Business card design needed

Family General Practitioner/ Family Physician.
Logo is the logo of the Crestmoor Guild of Family Clinicians Australia
http://kvplm.tarevo.edu.au/PictureGallery/logos/pages/CGFC%20logo_jpg.htm

Reason: Just a bit more time to make changes and the weekend for me to look at things closely and to choose. Thanks, Lumi

Thanks for all the submissions. So many of them are really works of art. Not one of them are not good. The ones that I am eliminating are the ones that I think are not suitable for me personally only, and because if I don't, it makes it very difficult to decide as many of you are also sending me slight variations of a card. I have just decided to choose a second place card too. Can't thank you all enough. Good luck, Lumi. P.S - Working today till 10 pm as the card says :-), so probably won't be able to give a feedback till late Saturday night or Sunday morning here in Sydney, Australia. 

Reason: Just added a second place to the budget and realised that Australia is ahead of the rest of the world in the time zone (only :-) - don't want to offend anyone or start a debate!! ) , so Monday deadline will mean it will be a weekend for the rest of the world. Just wanted to give everyone more time to submit their best, especially since I will be picking a second card too. Can't thank everyone enough for the submissions. P.S - Not keen on photos on the card.

Contact Information for Business Card

Dr. Lumi Harcourt M.B.B.S., F.C.G.F.C
Family General Practitioner
Address, timings, phone and fax number on the back.

Requirements
Must have
• Timings
Mon 7 am - 7 pm
Tues 7 am - 12 pm
Wed 7 am - 10 pm
Thurs 7 am - 12 pm
Fri 7 am - 8 pm
Sat 8 am - 10 pm
Sun - Off

```html
<!DOCTYPE html>
<html lang="en">
<head>
<meta charset="utf-8">
<title>Dr Lumi Harcourt – Business Card</title>
<link href="https://fonts.googleapis.com/css2?family=Libre+Bodoni:wght@400;500&display=swap" rel="stylesheet">
<style>
  :root {
    --page: #ffffff;
    --ink: #1c1c1c;
    --card-white: #ffffff;
    --card-edge: #b9cdd3;
    --card-grey: #a6adb0;
    --pattern-light: #c3c8ca;
    --crest-faint: #e6e6e6;
    --crest-faint-deep: #d2d2d2;
    --contact-red: #e2474a;
    --mark: #b0272d;
  }
  * { margin: 0; padding: 0; box-sizing: border-box; }
  html, body { width: 1200px; height: 655px; overflow: hidden; background: var(--page); }
  body { position: relative; font-family: "Libre Bodoni", "Bodoni 72", serif; color: var(--ink); }

  .card { position: absolute; overflow: hidden; }
  .card--light { background: var(--card-white); border: 1.5px solid var(--card-edge); }
  .card--grey { background: var(--card-grey); border-radius: 20px; }

  .front-light { left: 145px; top: 77px; width: 455px; height: 246px; }
  .front-grey  { left: 715px; top: 58px; width: 474px; height: 267px; }
  .back-light  { left: 137px; top: 366px; width: 452px; height: 245px; }
  .back-grey   { left: 711px; top: 372px; width: 469px; height: 267px; border-radius: 0 20px 20px 0; }

  .pattern { position: absolute; inset: 0; }

  .crest-faint { position: absolute; top: 0; height: 100%; }
  .front-light .crest-faint { left: 0; width: 128px; background: linear-gradient(90deg, var(--crest-faint-deep), var(--crest-faint) 70%, transparent); }
  .back-light .crest-faint { right: 0; width: 128px; background: linear-gradient(270deg, var(--crest-faint-deep), var(--crest-faint) 70%, transparent); }

  .guild-mark { position: absolute; display: flex; align-items: center; gap: 5px; font-size: 15px; font-weight: 500; color: var(--ink); }
  .guild-mark .square { width: 14px; height: 14px; background: var(--mark); }
  .front-light .guild-mark { right: 18px; top: 40px; }
  .front-grey .guild-mark { right: 26px; top: 62px; font-size: 19px; }
  .front-grey .guild-mark .square { width: 18px; height: 18px; }

  .identity { position: absolute; }
  .front-light .identity { right: 10px; top: 172px; text-align: right; }
  .front-grey .identity { left: 28px; top: 160px; }
  .doctor-name { font-size: 27px; font-weight: 400; line-height: 1; letter-spacing: 0.2px; }
  .credentials { font-size: 13px; line-height: 1.1; }
  .role { font-size: 16.5px; letter-spacing: 0.6px; margin-top: 12px; }
  .front-light .role { margin-top: 12px; }
  .front-grey .role { margin-top: 16px; }

  .hours { position: absolute; list-style: none; font-size: 16.5px; line-height: 20.7px; }
  .back-light .hours { left: 7px; top: 2px; }
  .back-grey .hours { left: 2px; top: 12px; }

  .address { position: absolute; font-size: 11.5px; line-height: 11.5px; font-style: normal; }
  .back-light .address { left: 6px; top: 186px; }
  .back-grey .address { left: 2px; top: 223px; font-size: 13px; line-height: 13px; }

  .contact-line { position: absolute; font-size: 10.5px; color: var(--contact-red); letter-spacing: 0.2px; }
  .back-light .contact-line { left: 6px; top: 222px; }
  .back-grey .contact-line { left: 2px; top: 246px; font-size: 11.5px; }
</style>
</head>
<body>

  <!-- Front, light version -->
  <section class="card card--light front-light">
    <div class="crest-faint" role="img" aria-label="Faint large crest decoration"></div>
    <div class="guild-mark"><span class="square"></span>CGFC</div>
    <div class="identity">
      <h1 class="doctor-name">Dr Lumi Harcourt</h1>
      <p class="credentials">M.B.B.S., F.C.G.F.C</p>
      <p class="role">FAMILY GENERAL PRACTITIONER</p>
    </div>
  </section>

  <!-- Front, grey version -->
  <section class="card card--grey front-grey">
    <svg class="pattern" role="img" aria-label="Soft grey animal-print pattern" width="474" height="267">
      <rect width="474" height="267" fill="var(--card-grey)"/>
    </svg>
    <div class="guild-mark"><span class="square"></span>CGFC</div>
    <div class="identity">
      <h1 class="doctor-name">Dr Lumi Harcourt</h1>
      <p class="credentials">M.B.B.S., F.C.G.F.C</p>
      <p class="role">FAMILY GENERAL PRACTITIONER</p>
    </div>
  </section>

  <!-- Back, light version -->
  <section class="card card--light back-light">
    <div class="crest-faint" role="img" aria-label="Faint large crest decoration"></div>
    <ul class="hours">
      <li>Working Hours</li>
      <li>Mon 7 am - 7 pm.</li>
      <li>Tues 7 am - 12 pm.</li>
      <li>Wed 7 am - 10 pm.</li>
      <li>Thurs 7 am - 12 pm.</li>
      <li>Fri 7 am - 8 pm.</li>
      <li>Sat 8 am - 10 pm.</li>
      <li>Sun - Off.</li>
    </ul>
    <address class="address">Level 2, Harbour Walk, Brindle Point Plaza<br>Wattlebrook, NSW 2190</address>
    <p class="contact-line">P: 02 9471 3580 &nbsp;F: 02 9471 3592</p>
  </section>

  <!-- Back, grey version -->
  <section class="card card--grey back-grey">
    <svg class="pattern" role="img" aria-label="Soft grey animal-print pattern" width="469" height="267">
      <rect width="469" height="267" fill="var(--card-grey)"/>
    </svg>
    <ul class="hours">
      <li>Working Hours</li>
      <li>Mon 7 am - 7 pm.</li>
      <li>Tues 7 am - 12 pm.</li>
      <li>Wed 7 am - 10 pm.</li>
      <li>Thurs 7 am - 12 pm.</li>
      <li>Fri 7 am - 8 pm.</li>
      <li>Sat 8 am - 10 pm.</li>
      <li>Sun - Off.</li>
    </ul>
    <address class="address">Level 2, Harbour Walk, Brindle Point Plaza<br>Wattlebrook, NSW 2190</address>
    <p class="contact-line">P: 02 9471 3580 &nbsp;F: 02 9471 3592</p>
  </section>

</body>
</html>
```